Real Estate Website

Peckford Realty will primarily be a residential rental and sales business.

Sales - Current properties - sold properties
Rentals - current properties - leased properties
Insights - Blog - Suburb profile
About us - Our agents
Working with us - rental/Sales

Here is a site that i like. Dont require video in the background.
https://www.mintowgate.com.au/
Scaled down version of this would be great. I like the landing page where it focuses on the client being vendor/landlord - not the buyers and sellers

Please make a banner on the home page that says 'request a free appraisal' with a button saying 'click here'.

I've attached some branding logos etc.
Brand colour is #f6ecd7 but using a white or black as the main of the website is fine.

```html
<!DOCTYPE html>
<html lang="en">
<head>
<meta charset="utf-8">
<title>Peckford Realty</title>
<link href="https://fonts.googleapis.com/css2?family=Marcellus&family=IBM+Plex+Sans:wght@400;500;600&display=swap" rel="stylesheet">
<style>
:root{
  --brand:#f6ecd7;
  --brand-soft:#f3e7cf;
  --ink:#1b1b1b;
  --muted:#6b6b6b;
  --white:#ffffff;
  --line:#bdbdbd;
  --stone:#a29c93;
  --badge-dark:#2f2f2f;
  --badge-sold:#ec1746;
  --badge-lease:#f39a1c;
}
*{margin:0;padding:0;box-sizing:border-box}
html,body{width:1200px;height:4208px;overflow:hidden}
body{position:relative;background:var(--white);font-family:"IBM Plex Sans",Arial,sans-serif;color:var(--ink)}
.abs{position:absolute}
.display{font-family:"Marcellus",Georgia,serif;font-weight:400;text-transform:uppercase;letter-spacing:1px}

/* header + hero */
.hero{left:0;top:0;width:1200px;height:687px;background:linear-gradient(180deg,#121212 0%,#2b2d2e 28%,#3f4446 55%,#35402f 80%,#2a2e2b 100%)}
.hero-shade{position:absolute;inset:0;background:rgba(0,0,0,.32)}
.brand-mark{font-family:"Marcellus",Georgia,serif;text-transform:uppercase;text-align:center;line-height:1}
.site-logo{left:144px;top:40px;width:207px;color:var(--white)}
.site-logo .l1{font-size:34px;letter-spacing:3px}
.site-logo .l2{font-size:26px;letter-spacing:4px;margin-top:2px}
.main-nav{top:60px;left:555px;display:flex;gap:0}
.main-nav a{color:var(--white);text-decoration:none;font-size:13.5px;font-weight:500;text-transform:uppercase;position:absolute;white-space:nowrap}
.main-nav a.active::after{content:"";position:absolute;left:0;right:0;bottom:-10px;height:3px;background:var(--white)}
.hero-title{left:0;width:1200px;top:296px;text-align:center;color:var(--white);font-size:68px}
.pill{display:flex;align-items:center;justify-content:center;background:var(--brand);color:var(--ink);border-radius:30px;font-size:14px;font-weight:600;text-transform:uppercase;text-decoration:none}
.hero-btn{left:519px;top:420px;width:162px;height:55px}
.dots{left:557px;top:608px;display:flex;gap:9px}
.dots span{width:9px;height:9px;border-radius:50%;background:var(--white)}
.dots span.ring{background:transparent;border:2px solid var(--white)}

/* section heading + tabs */
.section-title{left:0;width:1200px;text-align:center;font-size:64px;color:var(--ink)}
.tabs{left:0;width:1200px;height:40px}
.tab{position:absolute;top:0;height:40px;display:flex;align-items:center;justify-content:center;font-size:12.5px;font-weight:600;text-transform:uppercase;border:1.5px solid var(--line);background:var(--white)}
.tab.on{background:var(--brand);border-color:var(--brand)}

/* cards */
.card{position:absolute;width:289px;height:349px;background:var(--white);box-shadow:0 2px 6px rgba(0,0,0,.12)}
.card.feature{background:var(--brand-soft)}
.card-photo{height:198px;position:relative}
.card-body{padding:30px 32px 0}
.card-title{font-size:16.5px;font-weight:600;text-transform:uppercase;letter-spacing:.3px}
.card-text{margin-top:10px;font-size:13.5px;line-height:21px;color:var(--muted)}
.badge{position:absolute;top:20px;right:16px;height:28px;padding:0 9px;display:flex;align-items:center;font-size:12.5px;font-weight:600;color:var(--white);text-transform:uppercase}
.badge.current{background:var(--badge-dark)}
.badge.sold{background:var(--badge-sold)}
.badge.lease{background:var(--badge-lease)}
.badge.date{background:var(--badge-dark);border:2px solid var(--white)}
.view-all{left:0;width:1200px;text-align:center;font-size:16px;font-weight:600;text-transform:uppercase;display:flex;justify-content:center;align-items:center;gap:8px}

/* about */
.about{left:0;top:1470px;width:1200px;height:459px;background:var(--stone)}
.about-photo{position:absolute;left:560px;top:0;width:640px;height:459px;background:linear-gradient(90deg,var(--stone) 0%,#c9c2b8 22%,#d9d4cc 55%,#b8b5ae 80%,#8f9293 100%)}
.about-title{left:148px;top:1548px;color:var(--white);font-size:64px}
.about-text{left:148px;top:1660px;width:410px;color:var(--white);font-size:13.5px;line-height:21px}
.about-btn{left:148px;top:1780px;width:163px;height:55px}

/* working */
.working{left:0;top:2690px;width:1200px;height:459px;background:linear-gradient(135deg,#2f2a22 0%,#4a3f2c 30%,#3a3b36 55%,#4d3f27 80%,#2d2b26 100%)}
.working-shade{position:absolute;inset:0;background:rgba(20,22,28,.35)}
.working-title{left:0;width:1200px;top:2826px;text-align:center;color:var(--white);font-size:64px}
.working-btn{left:519px;top:2940px;width:162px;height:55px}

/* footer */
.site-footer{left:0;top:3851px;width:1200px;height:357px;background:var(--brand)}
.footer-logo{left:500px;top:3932px;width:200px;color:var(--ink)}
.footer-logo .l1{font-size:24px;letter-spacing:2px}
.footer-logo .l2{font-size:18px;letter-spacing:3px;margin-top:1px}
.footer-nav{left:0;width:1200px;top:4006px;text-align:center;font-size:21px;font-weight:500;text-transform:uppercase;letter-spacing:.5px}
.footer-nav .sep{margin:0 20px}
.legal{left:0;width:1200px;top:4060px;text-align:center;font-size:13.5px;color:#555}
.social{left:548px;top:4124px;display:flex;gap:14px}
.social span{width:24px;height:24px;border-radius:50%;background:var(--ink)}
</style>
</head>
<body>

<header class="abs hero" role="img" aria-label="Dusk aerial view of a suburban street of two-storey homes with parked cars">
  <div class="hero-shade"></div>
</header>
<div class="abs brand-mark site-logo"><div class="l1">Peckford</div><div class="l2">Realty</div></div>
<nav class="abs main-nav">
  <a class="active" style="left:0">Sales</a>
  <a style="left:75px">Rentals</a>
  <a style="left:167px">Insights</a>
  <a style="left:266px">About us</a>
  <a style="left:367px">Working with us</a>
</nav>
<h1 class="abs display hero-title">Request a free appraisal</h1>
<a class="abs pill hero-btn">Click here</a>
<div class="abs dots"><span></span><span></span><span class="ring"></span><span></span><span></span></div>

<!-- Sales -->
<h2 class="abs display section-title" style="top:772px">Sales</h2>
<div class="abs tabs" style="top:885px">
  <div class="tab on" style="left:323px;width:105px">All</div>
  <div class="tab" style="left:436px;width:217px">Current properties</div>
  <div class="tab" style="left:661px;width:216px">Sold properties</div>
</div>
<article class="card" style="left:144px;top:970px">
  <div class="card-photo" role="img" aria-label="Apartment towers around a landscaped pool" style="background:linear-gradient(160deg,#8fa8c4,#a7a296 55%,#4f6a3d)"><span class="badge current">Current</span></div>
  <div class="card-body"><h3 class="card-title">Sed ut perspiciatisu</h3><p class="card-text">Lorem ipsum dolor sit amet, consectetur adipiscing elit, sed do eiusmod tempor incididunt ut</p></div>
</article>
<article class="card feature" style="left:456px;top:970px">
  <div class="card-photo" role="img" aria-label="Row of grey gabled townhouses under a blue sky" style="background:linear-gradient(180deg,#1f4fa8,#5a6f8c 50%,#6e6a64)"></div>
  <div class="card-body"><h3 class="card-title">Voluptatem accusa</h3><p class="card-text">Lorem ipsum dolor sit amet, consectetur adipiscing elit, sed do eiusmod tempor incididunt ut</p></div>
</article>
<article class="card" style="left:767px;top:970px">
  <div class="card-photo" role="img" aria-label="Modern apartment block with balconies against the sky" style="background:linear-gradient(150deg,#2f7fc1,#7aa9cf 50%,#c9ced2)"><span class="badge sold">Sold</span></div>
  <div class="card-body"><h3 class="card-title">Laudantium totam</h3><p class="card-text">Lorem ipsum dolor sit amet, consectetur adipiscing elit, sed do eiusmod tempor incididunt ut</p></div>
</article>
<div class="abs view-all" style="top:1374px">View all
  <svg width="17" height="17" viewBox="0 0 17 17"><circle cx="8.5" cy="8.5" r="8.5" fill="#1b1b1b"/><path d="M7 4.8l3.6 3.7L7 12.2" stroke="#fff" stroke-width="2" fill="none"/></svg></div>

<!-- About -->
<section class="abs about">
  <div class="about-photo" role="img" aria-label="Agent shaking hands with a young couple in a bright living room"></div>
</section>
<h2 class="abs display about-title">About us</h2>
<p class="abs about-text">Lorem ipsum dolor sit amet, consectetur adipiscing elit, sed do eiusmod tempor incididunt ut labore et dolore magna aliqua. Quis ipsum suspendisse ultrices gravida. Risus commodo viverra maecenas accumsan lacus vel facilisis.</p>
<a class="abs pill about-btn">Read more</a>

<!-- Rentals -->
<h2 class="abs display section-title" style="top:2003px">Rentals</h2>
<div class="abs tabs" style="top:2116px">
  <div class="tab on" style="left:323px;width:105px">All</div>
  <div class="tab" style="left:436px;width:217px">Current properties</div>
  <div class="tab" style="left:661px;width:216px">Leased properties</div>
</div>
<article class="card" style="left:144px;top:2203px">
  <div class="card-photo" role="img" aria-label="Green-clad apartment building beside autumn trees" style="background:linear-gradient(180deg,#3d6fc0,#6f7d6c 50%,#4b5a3c)"><span class="badge current">Current</span></div>
  <div class="card-body"><h3 class="card-title">Sed ut perspiciatisu</h3><p class="card-text">Lorem ipsum dolor sit amet, consectetur adipiscing elit, sed do eiusmod tempor incididunt ut</p></div>
</article>
<article class="card feature" style="left:456px;top:2203px">
  <div class="card-photo" role="img" aria-label="Aerial view of a suburban housing estate" style="background:linear-gradient(135deg,#3c4a3a,#6a6f66 50%,#38443a)"></div>
  <div class="card-body"><h3 class="card-title">Voluptatem accusa</h3><p class="card-text">Lorem ipsum dolor sit amet, consectetur adipiscing elit, sed do eiusmod tempor incididunt ut</p></div>
</article>
<article class="card" style="left:767px;top:2203px">
  <div class="card-photo" role="img" aria-label="Contemporary apartment block with brick and timber facade" style="background:linear-gradient(150deg,#4a7fb8,#8a7a6a 55%,#5d564f)"><span class="badge lease">Lease</span></div>
  <div class="card-body"><h3 class="card-title">Laudantium totam</h3><p class="card-text">Lorem ipsum dolor sit amet, consectetur adipiscing elit, sed do eiusmod tempor incididunt ut</p></div>
</article>
<div class="abs view-all" style="top:2605px">View all
  <svg width="17" height="17" viewBox="0 0 17 17"><circle cx="8.5" cy="8.5" r="8.5" fill="#1b1b1b"/><path d="M7 4.8l3.6 3.7L7 12.2" stroke="#fff" stroke-width="2" fill="none"/></svg></div>

<!-- Working with us -->
<section class="abs working" role="img" aria-label="Aerial view of a leafy suburb in autumn">
  <div class="working-shade"></div>
</section>
<h2 class="abs display working-title">Working with us</h2>
<a class="abs pill working-btn">Read more</a>

<!-- Insights -->
<h2 class="abs display section-title" style="top:3234px">Insights</h2>
<article class="card" style="left:144px;top:3364px">
  <div class="card-photo" role="img" aria-label="Townhouse complex along a quiet street" style="background:linear-gradient(180deg,#6f9fd6,#7f7a6f 55%,#8a8c88)"><span class="badge date">Mar 2021</span></div>
  <div class="card-body"><h3 class="card-title">Minima veniam</h3><p class="card-text">Lorem ipsum dolor sit amet, consectetur adipiscing elit, sed do eiusmod tempor incididunt ut</p></div>
</article>
<article class="card" style="left:456px;top:3364px">
  <div class="card-photo" role="img" aria-label="Dark grey apartment building under a blue sky" style="background:linear-gradient(180deg,#2e5fae,#4b4f55 50%,#6b6d6e)"><span class="badge date">Mar 2021</span></div>
  <div class="card-body"><h3 class="card-title">Neque porro quisquam</h3><p class="card-text">Lorem ipsum dolor sit amet, consectetur adipiscing elit, sed do eiusmod tempor incididunt ut</p></div>
</article>
<article class="card" style="left:767px;top:3364px">
  <div class="card-photo" role="img" aria-label="Modern residential block with orange balconies" style="background:linear-gradient(150deg,#9ab6d4,#c9a27a 50%,#6c6c70)"><span class="badge date">Mar 2021</span></div>
  <div class="card-body"><h3 class="card-title">Ullam corporis suscipit</h3><p class="card-text">Lorem ipsum dolor sit amet, consectetur adipiscing elit, sed do eiusmod tempor incididunt ut</p></div>
</article>
<div class="abs view-all" style="top:3769px">View all insights
  <svg width="17" height="17" viewBox="0 0 17 17"><circle cx="8.5" cy="8.5" r="8.5" fill="#1b1b1b"/><path d="M7 4.8l3.6 3.7L7 12.2" stroke="#fff" stroke-width="2" fill="none"/></svg></div>

<!-- Footer -->
<footer class="abs site-footer"></footer>
<div class="abs brand-mark footer-logo"><div class="l1">Peckford</div><div class="l2">Realty</div></div>
<nav class="abs footer-nav">Sales<span class="sep">/</span>Rentals<span class="sep">/</span>Insights<span class="sep">/</span>About us<span class="sep">/</span>Working with us</nav>
<p class="abs legal">Copyright © 2021 - Peckford - All Rights Reserved &nbsp;|&nbsp; Privacy Policy &nbsp;|&nbsp; Terms and use</p>
<div class="abs social" aria-label="Social links"><span></span><span></span><span></span></div>

</body>
</html>
```